Registry Program Flyer design 2 - MV Linkway registry

We need two different flyers that will be distributed via web, email and print. This project is for the second of the two flyers.

The audience is patients and family members of patients with a specific disease. The flyer will be used to make patients aware of our web-based registry programs, and to inform/encourage patients to join.

An example prototype flyer with the text that should be used is attached. We would like to improve the design and layout of the flyer, while retaining as much of the language as appropriate.

The MVLinkway flyer should use the logo provided in the example and a color scheme compatible with the logo. The flyer may use the pictures included in the prototype.

If possible, a final format that allows us to edit the text is preferred. If this is not possible, we will finalize the text after receiving a prototype. Changes to the text will likely be minor.

Note: The design of the flyers for this project and the other project (Registry Program Flyer Design 1 - TRBQ registry) can be similar in style, however, they should not be duplicates.

Deliverables will be a final .PSD (photoshop) file with layers so we can edit text if necessary.

Target Market(s)

Physicians and healthcare professionals.

Requirements
Must have
• Use the attached logo and colors.

```html
<!DOCTYPE html>
<html lang="en">
<head>
<meta charset="utf-8">
<title>MV Linkway Registry Flyer</title>
<link href="https://fonts.googleapis.com/css2?family=Bebas+Neue&family=Open+Sans:wght@400;600;700&family=Roboto+Slab:wght@700;800&display=swap" rel="stylesheet">
<style>
:root{
  --red:#d31f26;
  --red-dark:#8e1116;
  --ink:#1b1b1b;
  --text:#333333;
  --white:#ffffff;
  --sky:#c9d6dc;
  --rock:#a89b86;
  --sponsor:#7a2a8c;
}
*{margin:0;padding:0;box-sizing:border-box}
html,body{width:934px;height:1200px;overflow:hidden;background:var(--white)}
.flyer{position:relative;width:934px;height:1200px;overflow:hidden;background:var(--white);font-family:"Open Sans",Arial,sans-serif;color:var(--text)}
.top-bar{position:absolute;left:0;top:0;width:934px;height:20px;background:var(--ink)}
.hero-photo{position:absolute;left:0;top:20px;width:934px;height:581px;
  background:linear-gradient(180deg,#e6ecef 0%,var(--sky) 30%,#b9b2a2 48%,var(--rock) 70%,#cdbfa8 100%)}
.brand{position:absolute;left:471px;top:58px;display:flex;align-items:center;gap:14px}
.brand-mark{width:60px;height:60px;background:var(--red)}
.brand-name{font-family:"Open Sans",Arial,sans-serif;font-weight:400;font-size:42px;color:var(--ink);line-height:1}
.fold{position:absolute}
.fold-top{left:500px;top:195px}
.fold-bottom{left:500px;top:1074px}
.panel{position:absolute;left:500px;top:223px;width:434px;height:852px;background:var(--red);color:var(--white);padding:22px 42px 0 26px}
.headline{font-family:"Bebas Neue",Impact,sans-serif;font-weight:400;font-size:68px;line-height:62px;text-align:center;letter-spacing:1px;color:var(--white);
  text-shadow:2px 2px 0 var(--ink),-1px -1px 0 var(--ink),1px -1px 0 var(--ink),-1px 1px 0 var(--ink)}
.panel h2{font-weight:700;font-size:18px;line-height:24px;margin-top:28px;margin-bottom:3px}
.panel p{font-size:13.4px;line-height:19.4px;text-align:justify}
.panel .lead-in{margin-top:20px;text-align:left}
.benefits{list-style:none;margin-top:3px}
.benefits li{position:relative;padding-left:28px;font-size:13.4px;line-height:22.3px;margin-bottom:0}
.benefits li::before{content:"";position:absolute;left:3px;top:6px;width:10px;height:10px;border-radius:50%;background:var(--white);box-shadow:inset 0 0 0 3px var(--red-dark)}
.panel .closing{margin-top:16px}
.tagline{font-family:"Roboto Slab",Georgia,serif;font-weight:800;font-size:18.5px !important;line-height:19.5px !important;text-align:center !important;margin-top:16px;text-shadow:1px 1px 0 var(--ink)}
.info{position:absolute;left:50px;top:616px;width:434px}
.info h3{font-family:"Roboto Slab",Georgia,serif;font-weight:700;font-size:21px;line-height:26px;color:var(--ink);margin-bottom:10px}
.info p{font-size:10.9px;line-height:15.8px;margin-bottom:14px;text-align:justify}
.audience{list-style:none;margin-bottom:20px}
.audience-row{display:flex;height:19px}
.audience li{font-size:10.9px;line-height:19px;padding-left:24px;position:relative}
.audience li::before{content:"";position:absolute;left:0;top:4px;width:11px;height:11px;border-radius:50%;background:var(--ink)}
.w1{width:83px}.w2{width:122px}.w3{width:189px}
.partners{position:absolute;left:55px;top:982px;display:flex;align-items:center}
.partner-name{display:flex;align-items:center;gap:8px;font-size:15px;font-weight:600;color:var(--ink);width:183px;line-height:17px}
.partner-name i{display:block;width:22px;height:22px;background:var(--red);flex:none}
.badge-round{width:58px;height:58px;border-radius:50%;background:#2e4f9c;margin-right:9px}
.badge-round.alt{background:#c3262c}
.badge-rect{width:98px;height:37px;border-radius:6px;background:#4ec3e6;margin-top:-20px}
.sponsor{position:absolute;left:51px;top:1040px}
.sponsor small{display:block;font-size:10.5px;color:var(--text);margin-left:45px}
.sponsor strong{display:block;font-size:22px;font-weight:600;color:var(--sponsor);margin-top:8px}
.footer-band{position:absolute;left:0;top:1144px;width:934px;height:56px;background:var(--red)}
.footer-bar{position:absolute;left:130px;top:1124px;width:688px;height:40px;background:var(--ink);border-radius:10px;display:flex;align-items:center;color:var(--white);font-size:12.5px}
.footer-item{display:flex;align-items:center;gap:10px;padding:0 20px;height:26px}
.footer-item+.footer-item{border-left:1px solid #777}
.footer-item:first-child{width:200px}
.footer-item:nth-child(2){width:238px}
</style>
</head>
<body>
<div class="flyer">
  <div class="top-bar"></div>
  <div class="hero-photo" role="img" aria-label="Photo of two women walking together along a rocky seashore"></div>

  <div class="brand">
    <span class="brand-mark"></span>
    <span class="brand-name">MV Linkway</span>
  </div>

  <svg class="fold fold-top" width="96" height="28" viewBox="0 0 96 28"><polygon points="0,28 96,0 96,28" fill="var(--red-dark)"/></svg>
  <section class="panel">
    <h1 class="headline">Join<br>MVLinkway.org<br>Today !</h1>
    <h2>Get Connected</h2>
    <p>One of the most important steps towards finding effective treatments for lipodystrophy (LD) is to uncover the ways in which the diseases behave, the symptoms that are commonly seen and how those symptoms progress. This requires the collection of as much information as possible about all people affected by LD. MV Linkway will serve as that database–the critical link between the patient community and the scientific community. The more people who join the registry the greater the chances that research will produce results that benefit everyone.</p>
    <p class="lead-in">Join THE LINKWAY TRBQ Registry to:</p>
    <ul class="benefits">
      <li>Tell us about your experience with LD and learn about the experiences with others</li>
      <li>Share information in a program that protects your privacy</li>
      <li>Provide valuable quality-of-life information that can be used to advocate on behalf of the LD community</li>
      <li>Help the research community launch clinical trials and studies</li>
    </ul>
    <p class="closing">We need to hear YOUR VOICE and we hope you will decide to join MV Linkway. Every individual who joins makes a vital contribution toward helping all of those affected by lipodystrophy.</p>
    <p class="tagline">Your information will lead to future treatments and cures for all types of Lipodystrophy</p>
  </section>
  <svg class="fold fold-bottom" width="96" height="30" viewBox="0 0 96 30"><polygon points="0,0 96,0 96,30" fill="var(--red-dark)"/></svg>

  <section class="info">
    <h3>Who Can Participate</h3>
    <ul class="audience">
      <div class="audience-row">
        <li class="w1">Patients</li>
        <li class="w2">Family members</li>
        <li>Healthcare providers</li>
      </div>
      <div class="audience-row">
        <li class="w3">Investigators &amp; researchers</li>
        <li>All stakeholders interested in TRBQ</li>
      </div>
    </ul>
    <h3>How it Works</h3>
    <p>Patients can join the registry to submit their data. After taking web-based surveys, explore the collected information in a way that protects the privacy of everyone.</p>
    <h3 style="margin-top:22px">Who We Are</h3>
    <p>As its name implies, MV Linkway represents the coming together of a wide range of entities and individuals who recognize the value in pooling their combined expertise and information. The Governing Board of MV Linkway comes from leaders in the non-profit sector, government agencies and academic institutions.</p>
    <p>Regardless of their individual backgrounds, the thought leaders of MV Linkway share a common goal to increase the community's ability to help one another through improved communication, and by doing so, to help the millions of people affected by Lipodystrophy.</p>
  </section>

  <div class="partners">
    <span class="partner-name"><i></i>Allied Patients United</span>
    <span class="badge-round"></span>
    <span class="badge-round alt"></span>
    <span class="badge-rect"></span>
  </div>
  <div class="sponsor">
    <small>Sponsored by:</small>
    <strong>Norvel Pharma</strong>
  </div>

  <div class="footer-band"></div>
  <div class="footer-bar">
    <div class="footer-item">
      <svg width="18" height="18" viewBox="0 0 18 18" fill="none" stroke="#fff" stroke-width="1.4"><circle cx="9" cy="9" r="7.5"/><ellipse cx="9" cy="9" rx="3.2" ry="7.5"/><line x1="1.5" y1="9" x2="16.5" y2="9"/></svg>
      <span>www.TRBQRegistry.org</span>
    </div>
    <div class="footer-item">
      <svg width="18" height="14" viewBox="0 0 18 14"><rect x="0" y="0" width="18" height="14" fill="#fff"/><polyline points="0,0 9,8 18,0" fill="none" stroke="var(--ink)" stroke-width="1.4"/></svg>
      <span>info@carejunction.com</span>
    </div>
    <div class="footer-item">
      <svg width="18" height="18" viewBox="0 0 18 18" fill="none" stroke="#fff" stroke-width="1.6"><circle cx="9" cy="9" r="7.5"/><path d="M11.6 6.6a3.4 3.4 0 1 0 0 4.8"/></svg>
      <span>Copyright © 2014 CareJunction</span>
    </div>
  </div>
</div>
</body>
</html>
```